IT Professional business card with a hometown feel and a little edgy.

My business name is Tamble Website Solutions. But I have ended up doing much more. I live in a very small remote community, where everyone knows everyone. We like the one-on-one customer service in this community. I do computer tutoring, virus removal, networking, and software training. My clients are businesses and private individuals.

My website is tamblewebsitesolutions.example, when I first designed it I was going for a fresh, clean look, which I still like. But I am thinking about making the website a bit more edgy to match my new logo from ArtHively (logo attached). At this time my website does not display the new logo, but I plan on redesigning the website in the future to match the logo and business card.

My tag line is "put the web to work for you"

I'm thinking I would like to have the business card printed with a metallic finish.
Updates

Please do not use black backgrounds, or any solid dark colors. Prefer light or white backgrounds.

Target Market(s)

Small businesses. Individuals that need computer help at home.

Industry/Entity Type

It Company

Contact Information for Business Card

Nora Prandell
Tamble Website Solutions
PO Box 7153
Ravel, WA 98364
Cell: 555-271-3096
nora@tamblewebsitesolutions.example
tamblewebsitesolutions.example

Font styles to use
Serif

Requirements
Must have
• Must have all the information listed in "Business Card Details"
• Must use the logo provided.
• Use the colors from the provided logo
Nice to have
• Would like to use my tagline "put the web to work for you" all lowercase

```html
<!DOCTYPE html>
<html lang="en">
<head>
<meta charset="utf-8">
<title>Tamble Website Solutions – Business Card</title>
<link rel="stylesheet" href="https://fonts.googleapis.com/css2?family=Della+Respira&display=swap">
<style>
  :root {
    --green: #3c7a3a;
    --green-dark: #2f6a30;
    --ink: #2b2b2b;
    --rule: #555555;
    --paper: #ffffff;
    --bezel-light: #d9d9d9;
    --bezel-mid: #b8b8b8;
    --bezel-dark: #9a9a9a;
    --dot: #f2f2f2;
  }
  * { box-sizing: border-box; margin: 0; padding: 0; }
  html, body { width: 1200px; height: 340px; overflow: hidden; background: #ffffff; }
  .canvas { position: relative; width: 1200px; height: 340px; font-family: "Della Respira", serif; }

  .card-side {
    position: absolute; top: 0; height: 340px; width: 594px;
    background: linear-gradient(180deg, var(--bezel-dark) 0%, var(--bezel-light) 45%, var(--bezel-mid) 100%);
    overflow: hidden;
  }
  .card-front { left: 0; }
  .card-back { left: 606px; }

  .front-screen {
    position: absolute; left: 28px; top: 25px; width: 538px; height: 283px;
    background: var(--paper);
  }
  .brand-square {
    position: absolute; left: 150px; top: 105px; width: 74px; height: 74px;
    background: var(--green);
  }
  .brand-divider {
    position: absolute; left: 318px; top: 60px; width: 2px; height: 168px;
    background: var(--rule);
  }
  .brand-name {
    position: absolute; left: 340px; top: 104px;
    font-size: 26px; line-height: 29px; color: var(--green);
  }
  .tagline {
    position: absolute; left: 0; right: 0; top: 219px; text-align: center;
    font-size: 23px; color: var(--ink);
  }
  .bezel-dots { position: absolute; left: 506px; top: 317px; display: flex; gap: 4px; }
  .bezel-dots span { width: 8px; height: 8px; border-radius: 50%; background: var(--dot); }

  .back-decoration {
    position: absolute; left: 30px; top: 40px; width: 420px; height: 260px;
    background: radial-gradient(ellipse at 40% 50%, rgba(255,255,255,0.35), rgba(255,255,255,0) 70%);
  }
  .contact-panel {
    position: absolute; left: 104px; top: 79px; width: 490px; height: 185px;
    background: var(--paper); padding: 13px 0 0 50px;
  }
  .contact-list { list-style: none; }
  .contact-item {
    display: flex; align-items: center; height: 39.5px;
    font-size: 15px; color: var(--ink); white-space: nowrap;
  }
  .contact-icon { width: 24px; height: 24px; margin-right: 12px; flex: none; fill: var(--green-dark); }
</style>
</head>
<body>
<main class="canvas">
  <section class="card-side card-front">
    <div class="front-screen">
      <span class="brand-square"></span>
      <span class="brand-divider"></span>
      <p class="brand-name">Tamble<br>Website<br>Solutions</p>
      <p class="tagline">"put the web to work for you"</p>
    </div>
    <div class="bezel-dots"><span></span><span></span><span></span></div>
  </section>

  <section class="card-side card-back">
    <div class="back-decoration" role="img" aria-label="Faint monitor motif in soft grey"></div>
    <div class="contact-panel">
      <ul class="contact-list">
        <li class="contact-item">
          <svg class="contact-icon" viewBox="0 0 24 24" aria-hidden="true"><path d="M12 2a7 7 0 0 0-7 7c0 5 7 13 7 13s7-8 7-13a7 7 0 0 0-7-7zm0 9.5A2.5 2.5 0 1 1 12 6.5a2.5 2.5 0 0 1 0 5z"/></svg>
          Tamble Website Solutions, PO Box 7153 Ravel, WA 98364
        </li>
        <li class="contact-item">
          <svg class="contact-icon" viewBox="0 0 24 24" aria-hidden="true"><path d="M2 7c0-2 4-3 10-3s10 1 10 3v2h-5V7.5c-1.5-.4-3-.5-5-.5s-3.5.1-5 .5V9H2zM6 10h12l3 9H3zm6 2.5a2.5 2.5 0 1 0 0 5 2.5 2.5 0 0 0 0-5z"/></svg>
          555-271-3096
        </li>
        <li class="contact-item">
          <svg class="contact-icon" viewBox="0 0 24 24" aria-hidden="true"><path d="M2 5h20v14H2zm2 2v.5l8 5.5 8-5.5V7z"/></svg>
          nora@tamblewebsitesolutions.example
        </li>
        <li class="contact-item">
          <svg class="contact-icon" viewBox="0 0 24 24" aria-hidden="true"><circle cx="12" cy="12" r="10"/><path d="M8 6c2 1 1 3 3 3s1 3-1 3-2 3 0 5M15 5c-1 2 1 3 3 3M16 13c-1 1 0 3 1 4" stroke="#fff" stroke-width="1.6" fill="none"/></svg>
          tamblewebsitesolutions.example
        </li>
      </ul>
    </div>
  </section>
</main>
</body>
</html>
```